looking to have a web site for the company which provides services in the industrial and commercial sectors such as: electrical, automation control and system integration, construction and maintenance, millwright, equipment assembly repair and installation. I have the domain already brivanholdings.net and logo. Most recent projects fulfilled for the following clients: MarlowKibbleCo, Dunholt University, OKSU, FALSTO, Tazzik, Prairie Grains

Target Market(s)

industrial and commercial sectors in electrical, automation, millwright and fabrication fields

Industry/Entity Type

Industrial

Coding

Coded - Design and coding required

Number of Pages Required

5+ page

Font styles to use
Sans Serif

Colors

Designer to choose colors to be used in the design.

Requirements
Nice to have
• looking to get something not complicated, nicely presented with minimum or no scrolling

```html
<!DOCTYPE html>
<html lang="en">
<head>
<meta charset="utf-8">
<title>Brivan Holdings</title>
<link rel="stylesheet" href="https://fonts.googleapis.com/css2?family=Open+Sans:ital,wght@0,400;0,600;0,700;1,600&display=swap">
<style>
:root{
  --brand:#155f9c;
  --brand-bright:#1f8fd6;
  --ink:#3a3a3a;
  --muted:#555;
  --line:#2f2f2f;
  --panel:#f2f2f2;
  --white:#fff;
  --steel-dark:#4b5056;
  --steel-light:#a9adb1;
}
*{box-sizing:border-box;margin:0;padding:0}
html,body{width:1200px;height:2560px;overflow:hidden;background:var(--white)}
body{font-family:"Open Sans",Arial,sans-serif;color:var(--ink);position:relative}
.site-header{height:111px;position:relative}
.brand-logo{position:absolute;left:77px;top:30px;font-weight:700;font-size:30px;color:var(--brand);letter-spacing:1px;line-height:1.1}
.brand-logo small{display:block;font-size:17px;letter-spacing:6px}
.main-nav{position:absolute;right:64px;top:44px;display:flex;gap:8px}
.main-nav a{font-size:14px;font-weight:700;color:#333;text-decoration:none;padding:8px 20px;border-radius:18px;text-transform:uppercase}
.main-nav a.active{background:linear-gradient(#2ea3e6,#0d6db6);color:var(--white)}
.hero{position:absolute;top:111px;left:0;width:1200px;height:538px;background:linear-gradient(100deg,#6f7377 0%,#9ca0a3 35%,#b9bcbf 60%,#c9ccce 80%,#7f8a6a 100%)}
.hero-title{position:absolute;top:222px;width:100%;text-align:center;color:var(--white);font-size:36px;font-weight:700;line-height:44px;text-transform:uppercase;text-shadow:0 2px 4px rgba(0,0,0,.35)}
.hero-dots{position:absolute;top:496px;width:100%;display:flex;justify-content:center;gap:8px}
.hero-dots span{width:11px;height:11px;border-radius:50%;background:var(--white)}
.hero-dots span.on{background:var(--brand-bright)}
.section-title{font-size:26px;font-weight:700;color:var(--brand);text-align:center;text-transform:uppercase}
.section-title::after{content:"";display:block;width:90px;height:3px;background:var(--line);margin:14px auto 0}
.welcome{position:absolute;top:688px;width:100%}
.welcome p{width:1050px;margin:26px auto 0;text-align:center;font-size:16px;line-height:27px;color:var(--muted)}
.btn{display:block;width:179px;height:46px;line-height:46px;border-radius:23px;text-align:center;background:linear-gradient(#2ea3e6,#0d6db6);color:var(--white);font-weight:700;font-size:15px;text-transform:uppercase;text-decoration:none}
.welcome .btn{margin:24px auto 0}
.services{position:absolute;top:985px;width:1200px;height:463px;background:var(--panel)}
.services-photo{position:absolute;left:0;top:0;width:600px;height:463px;background:linear-gradient(100deg,#2e3236,#45494d 45%,#3a3e40)}
.services-intro{position:absolute;left:0;top:125px;width:600px;text-align:center;color:var(--white)}
.services-intro h2{font-size:25px;font-weight:700;text-transform:uppercase}
.services-intro h2::after{content:"";display:block;width:60px;height:3px;background:var(--white);margin:12px auto 0}
.services-intro p{font-size:18px;line-height:27px;margin:18px auto 0;width:400px}
.services-intro .btn{margin:16px auto 0;width:180px}
.service-item{position:absolute;left:557px;width:600px;display:flex}
.service-icon{width:88px;height:88px;border-radius:50%;background:var(--white);border:3px solid var(--brand);flex:none;display:flex;align-items:center;justify-content:center}
.service-text{margin-left:31px;margin-top:-14px}
.service-text h3{font-size:16px;font-weight:600;color:var(--brand);text-transform:uppercase}
.service-text p{font-size:13.5px;line-height:24px;color:var(--muted);margin-top:4px;width:460px}
.clients{position:absolute;top:1488px;width:100%}
.clients .lead{text-align:center;font-size:16px;color:var(--muted);margin-top:30px}
.client-grid{position:absolute;top:130px;left:75px;width:1050px}
.client-box{position:absolute;width:241px;height:103px;border:1px solid #ddd;border-radius:10px;display:flex;align-items:center;justify-content:center;gap:8px;font-size:20px;font-weight:700;color:var(--ink)}
.client-box i{width:14px;height:14px;background:var(--brand);display:block}
.blog{position:absolute;top:1905px;width:1200px;height:382px;background:var(--panel)}
.blog .section-title{margin-top:46px}
.post{position:absolute;top:133px;width:510px}
.post-photo{position:absolute;left:0;top:0;width:241px;height:174px;border-radius:10px;background:linear-gradient(135deg,#5b5650,#8f8a86 50%,#3d4146)}
.post-body{position:absolute;left:270px;top:-6px;width:250px}
.post-body h3{font-size:16px;font-weight:600;color:var(--brand);line-height:26px;text-transform:uppercase}
.post-body p{font-size:14px;line-height:24px;color:var(--muted);margin-top:6px}
.post-body a{display:block;margin-top:8px;font-size:14px;font-weight:600;font-style:italic;color:#222;text-decoration:none}
.site-footer{position:absolute;top:2287px;width:1200px;height:273px}
.footer-brand{position:absolute;left:77px;top:60px}
.footer-brand .brand-logo{position:static;font-size:26px}
.footer-brand p{font-size:12px;line-height:20px;color:var(--muted);margin-top:20px}
.social{display:flex;gap:16px;margin-top:18px}
.social span{width:18px;height:18px;border-radius:50%;background:#8a8a8a;display:block}
.footer-col{position:absolute;top:46px}
.footer-col h4{font-size:14px;font-weight:700;color:var(--brand);text-transform:uppercase;margin-bottom:14px}
.footer-col li{list-style:none;font-size:13px;line-height:26px;color:#333}
.news-item{font-size:13px;line-height:21px;color:#333;margin-bottom:14px;width:220px}
.news-item span{display:block;font-size:11px;font-weight:700;color:var(--brand)}
.contact-row{display:flex;align-items:center;gap:18px;font-size:13px;line-height:21px;color:#333;margin-bottom:10px}
.contact-row svg{flex:none}
</style>
</head>
<body>
<header class="site-header">
  <div class="brand-logo">BRIVAN<small>HOLDINGS</small></div>
  <nav class="main-nav">
    <a class="active" href="#">Home</a><a href="#">About Us</a><a href="#">Services</a><a href="#">Blog</a><a href="#">Clients</a><a href="#">Contact Us</a>
  </nav>
</header>

<section class="hero" role="img" aria-label="Photograph of corrugated steel grain silos and an industrial loading tower under a cloudy sky">
  <h1 class="hero-title">Nam fermentum vestibulum<br>purus id aliquet</h1>
  <div class="hero-dots"><span class="on"></span><span></span><span></span><span></span></div>
</section>

<section class="welcome">
  <h2 class="section-title">Welcome to our website</h2>
  <p>Aliquam molestie, mi et imperdiet euismod, dui purus auctor tellus, et interdum lacus lectus et ante. Sed accumsan sollicitudin sapien, sit amet adipiscing turpis gravida ac. In congue, neque ac lobortis volutpat, libero mauris varius mi, vitae suscipit ipsum ligula vitae risus. Duis aliquam nibh a dui iaculis viverra id a velit. Vivamus egestas risus in magna varius commodo. Sed semper viverra egestas. Etiam pretium porttitor lectus, vel ornare neque porta volutpat.</p>
  <a class="btn" href="#">Read More</a>
</section>

<section class="services">
  <div class="services-photo" role="img" aria-label="Darkened photograph of steel grain silos at an industrial site"></div>
  <div class="services-intro">
    <h2>Our Services</h2>
    <p>We provide services in the industrial and commercial sectors such as.</p>
    <a class="btn" href="#">Read More</a>
  </div>
  <div class="service-item" style="top:55px">
    <div class="service-icon"><svg width="40" height="40" viewBox="0 0 40 40"><circle cx="20" cy="20" r="17" fill="none" stroke="#222" stroke-width="3"/><path d="M23 7 L12 22 H19 L16 33 L28 17 H21 Z" fill="#222"/></svg></div>
    <div class="service-text"><h3>Electrical</h3><p>Aliquam molestie, mi et imperdiet euismod, dui purus auctor tellus, et interdum lacus lectus et ante. Sed accumsan sollicitudin sapien, sit amet adipiscing turpis gravida ac</p></div>
  </div>
  <div class="service-item" style="top:183px">
    <div class="service-icon"><svg width="42" height="42" viewBox="0 0 42 42"><g fill="#222"><circle cx="16" cy="24" r="9"/><circle cx="30" cy="12" r="6"/></g><g stroke="#222" stroke-width="4"><path d="M16 11v26M3 24h26M7 15l18 18M25 15 7 33"/><path d="M30 3v18M21 12h18M24 6l12 12M36 6 24 18" stroke-width="3"/></g><circle cx="16" cy="24" r="3.5" fill="#fff"/><circle cx="30" cy="12" r="2.5" fill="#fff"/></svg></div>
    <div class="service-text"><h3>Automation Control &amp; System Integration</h3><p>Aliquam molestie, mi et imperdiet euismod, dui purus auctor tellus, et interdum lacus lectus et ante. Sed accumsan sollicitudin sapien, sit amet adipiscing turpis gravida ac</p></div>
  </div>
  <div class="service-item" style="top:311px">
    <div class="service-icon"><svg width="40" height="40" viewBox="0 0 40 40"><path d="M27 5a8 8 0 0 0-7 11L6 30a3 3 0 0 0 4 4l14-14a8 8 0 0 0 11-7l-5 3-4-2-1-4z" fill="#222"/><rect x="4" y="34" width="32" height="3" fill="#222"/></svg></div>
    <div class="service-text"><h3>Construction &amp; Maintenance</h3><p>Aliquam molestie, mi et imperdiet euismod, dui purus auctor tellus, et interdum lacus lectus et ante. Sed accumsan sollicitudin sapien, sit amet adipiscing turpis gravida ac</p></div>
  </div>
</section>

<section class="clients">
  <h2 class="section-title">Our Clients</h2>
  <p class="lead">Aliquam molestie, mi et imperdiet euismod, dui purus auctor tellus, et interdum lacus lectus et ante.</p>
  <div class="client-grid">
    <div class="client-box" style="left:0;top:0">Tazzik</div>
    <div class="client-box" style="left:270px;top:0"><i></i>MarlowKibbleCo</div>
    <div class="client-box" style="left:540px;top:0">OKSU</div>
    <div class="client-box" style="left:809px;top:0">Prairie Grains</div>
    <div class="client-box" style="left:270px;top:128px">Dunholt University</div>
    <div class="client-box" style="left:540px;top:128px"><i></i>FALSTO</div>
  </div>
</section>

<section class="blog">
  <h2 class="section-title">Blog Posts</h2>
  <article class="post" style="left:75px">
    <div class="post-photo" role="img" aria-label="Photograph of pipework and machinery inside an industrial plant"></div>
    <div class="post-body"><h3>Aenean a nibh eget turpis vehicula tempus</h3><p>Aliquam molestie, mi et imperdiet euismod, dui purus auctor tellus, et interdum lacus lectussed accumsan sollicitudin sapien..</p><a href="#">Continue Reading</a></div>
  </article>
  <article class="post" style="left:615px">
    <div class="post-photo" style="background:linear-gradient(135deg,#3f4448,#9aa0a4 55%,#5a5f63)" role="img" aria-label="Photograph of wrapped equipment on a factory floor"></div>
    <div class="post-body"><h3>Aenean a nibh eget turpis vehicula tempus</h3><p>Aliquam molestie, mi et imperdiet euismod, dui purus auctor tellus, et interdum lacus lectussed accumsan sollicitudin sapien..</p><a href="#">Continue Reading</a></div>
  </article>
</section>

<footer class="site-footer">
  <div class="footer-brand">
    <div class="brand-logo">BRIVAN<small>HOLDINGS</small></div>
    <p>Copyright © 2017. Company Name<br>All Right Reserved</p>
    <div class="social"><span></span><span></span><span></span><span></span><span></span></div>
  </div>
  <div class="footer-col" style="left:360px">
    <h4>Site Map</h4>
    <ul><li>Home</li><li>About Us</li><li>Services</li><li>Blog</li><li>Clients</li><li>Contact Us</li></ul>
  </div>
  <div class="footer-col" style="left:543px">
    <h4>Latest News</h4>
    <div class="news-item">Vestibulum ante ipsum primis in faucibus orci luctus..<span>Oct 12, 2017</span></div>
    <div class="news-item">Vestibulum ante ipsum primis in faucibus orci luctus..<span>Oct 12, 2017</span></div>
  </div>
  <div class="footer-col" style="left:818px">
    <h4>Contact Info</h4>
    <div class="contact-row" style="margin-bottom:14px">4120 Kessler Road,<br>Glasgow, D07 41KT</div>
    <div class="contact-row"><svg width="12" height="12" viewBox="0 0 12 12"><path d="M2 1l2 0 1 3-1.5 1a7 7 0 0 0 3.5 3.5L8 7l3 1v2a1 1 0 0 1-1 1A9 9 0 0 1 1 2a1 1 0 0 1 1-1z" fill="#333"/></svg>1-800-555-0142</div>
    <div class="contact-row"><svg width="12" height="10" viewBox="0 0 12 10"><rect width="12" height="10" fill="#333"/><path d="M0 0l6 5 6-5" stroke="#fff" fill="none"/></svg>info@brivanholdings.net</div>
    <div class="contact-row"><svg width="12" height="14" viewBox="0 0 12 14"><path d="M6 0a5 5 0 0 1 5 5c0 4-5 9-5 9S1 9 1 5a5 5 0 0 1 5-5z" fill="#333"/><circle cx="6" cy="5" r="2" fill="#fff"/></svg>Map Location</div>
  </div>
</footer>
</body>
</html>
```